Property Management business needs Business cards designed

We provide a premium property management service based in Sydney's Norther Beaches. We want people to feel confident in choosing us to manage their investment properties. We offer a much more personalized service than other estate agents.
We want a modern clean design. Something that shows confidence without being complicated.
Logo attached.

Target Market(s)

35-70yo Male and Female with strong property portfolios within Sydney's Norther Beaches

Industry/Entity Type

Property Management

Contact Information for Business Card

Address: Suite 7, 12-14 Kelvin Parade, Harlow NSW 2188
Two separate named cards.
Tom Ardley - 0491 570 118 tom@harbourvaleestates.com.au
Clara Dunmore - 0491 570 263 clara@harbourvaleestates.com.au

Requirements
Must have
• Business logo, name, number, address, email.

```html
<!DOCTYPE html>
<html lang="en">
<head>
<meta charset="utf-8">
<title>Harbourvale Estates – Business Cards</title>
<link href="https://fonts.googleapis.com/css2?family=Arimo:wght@400;700&display=swap" rel="stylesheet">
<style>
  :root {
    --teal: #2a8c9c;
    --ink: #161616;
    --card: #ffffff;
    --backdrop: #2b2b2d;
    --edge: #dcdcdc;
    --edge-deep: #cfcfcf;
  }
  * { box-sizing: border-box; margin: 0; padding: 0; }
  html, body { width: 1200px; height: 900px; overflow: hidden; }
  body {
    background: var(--backdrop);
    font-family: "Arimo", Arial, sans-serif;
    position: relative;
  }
  .business-card {
    position: absolute;
    width: 680px;
    height: 390px;
    background: var(--card);
    border-radius: 22px;
    box-shadow: 0 3px 0 var(--edge), 0 6px 0 var(--edge-deep), 0 18px 36px rgba(0,0,0,0.45);
    color: var(--ink);
  }
  .card-tom { left: 60px; top: 36px; }
  .card-clara { left: 460px; top: 468px; }

  .holder {
    position: absolute;
    right: 80px;
    top: 44px;
    text-align: right;
  }
  .holder-name {
    color: var(--teal);
    font-size: 30px;
    font-weight: 400;
    letter-spacing: 0.3px;
  }
  .holder-role {
    font-size: 17px;
    margin-top: 2px;
  }

  .brand {
    position: absolute;
    left: 66px;
    top: 146px;
    display: flex;
    align-items: center;
    gap: 12px;
  }
  .brand-mark {
    width: 16px;
    height: 16px;
    background: var(--teal);
  }
  .brand-name {
    font-size: 32px;
    font-weight: 700;
    color: var(--ink);
    letter-spacing: 0.5px;
  }

  .contact-list {
    position: absolute;
    left: 355px;
    top: 206px;
    list-style: none;
    font-size: 17px;
  }
  .contact-list li {
    display: flex;
    align-items: center;
    gap: 12px;
    height: 28px;
    white-space: nowrap;
  }
  .contact-list svg { width: 17px; height: 17px; flex: none; }

  .office {
    position: absolute;
    left: 66px;
    bottom: 48px;
    font-size: 19px;
    font-style: normal;
    line-height: 1.25;
  }
  .office-name { color: var(--teal); }
</style>
</head>
<body>

  <article class="business-card card-tom">
    <header class="holder">
      <p class="holder-name">Tom Ardley</p>
      <p class="holder-role">Director</p>
    </header>
    <div class="brand">
      <span class="brand-mark"></span>
      <span class="brand-name">HARBOURVALE ESTATES</span>
    </div>
    <ul class="contact-list">
      <li>
        <svg viewBox="0 0 24 24" fill="var(--teal)"><path d="M6.6 10.8a15 15 0 0 0 6.6 6.6l2.2-2.2c.3-.3.7-.4 1-.2 1.1.4 2.3.6 3.6.6.6 0 1 .4 1 1V20c0 .6-.4 1-1 1A17 17 0 0 1 3 4c0-.6.4-1 1-1h3.5c.6 0 1 .4 1 1 0 1.3.2 2.5.6 3.6.1.3 0 .7-.2 1z"/></svg>
        <span>0491 570 118</span>
      </li>
      <li>
        <svg viewBox="0 0 24 24"><rect x="2" y="5" width="20" height="14" rx="1" fill="var(--teal)"/><path d="M2.5 6l9.5 7 9.5-7" stroke="#fff" stroke-width="1.6" fill="none"/></svg>
        <span>tom@harbourvaleestates.com.au</span>
      </li>
      <li>
        <svg viewBox="0 0 24 24" fill="none" stroke="var(--teal)" stroke-width="2"><circle cx="12" cy="12" r="9"/><ellipse cx="12" cy="12" rx="4" ry="9"/><path d="M3 12h18M5 7h14M5 17h14"/></svg>
        <span>www.harbourvaleestates.com</span>
      </li>
    </ul>
    <address class="office">
      <span class="office-name">Harbourvale Estates</span><br>
      Suite 7, 12-14 Kelvin Parade<br>
      Harlow NSW 2188
    </address>
  </article>

  <article class="business-card card-clara">
    <header class="holder">
      <p class="holder-name">Clara Dunmore</p>
      <p class="holder-role">Director</p>
    </header>
    <div class="brand">
      <span class="brand-mark"></span>
      <span class="brand-name">HARBOURVALE ESTATES</span>
    </div>
    <ul class="contact-list">
      <li>
        <svg viewBox="0 0 24 24" fill="var(--teal)"><path d="M6.6 10.8a15 15 0 0 0 6.6 6.6l2.2-2.2c.3-.3.7-.4 1-.2 1.1.4 2.3.6 3.6.6.6 0 1 .4 1 1V20c0 .6-.4 1-1 1A17 17 0 0 1 3 4c0-.6.4-1 1-1h3.5c.6 0 1 .4 1 1 0 1.3.2 2.5.6 3.6.1.3 0 .7-.2 1z"/></svg>
        <span>0491 570 263</span>
      </li>
      <li>
        <svg viewBox="0 0 24 24"><rect x="2" y="5" width="20" height="14" rx="1" fill="var(--teal)"/><path d="M2.5 6l9.5 7 9.5-7" stroke="#fff" stroke-width="1.6" fill="none"/></svg>
        <span>clara@harbourvaleestates.com.au</span>
      </li>
      <li>
        <svg viewBox="0 0 24 24" fill="none" stroke="var(--teal)" stroke-width="2"><circle cx="12" cy="12" r="9"/><ellipse cx="12" cy="12" rx="4" ry="9"/><path d="M3 12h18M5 7h14M5 17h14"/></svg>
        <span>www.harbourvaleestates.com</span>
      </li>
    </ul>
    <address class="office">
      <span class="office-name">Harbourvale Estates</span><br>
      Suite 7, 12-14 Kelvin Parade<br>
      Harlow NSW 2188
    </address>
  </article>

</body>
</html>
```